Stainless Steel Business Card

I have a fiber laser and want to highlight its capabilities in a business card. On the card I want

Brisler Systems
Martin Pelko
martin@mpelkoworks.com
417-555-0136

This will be cut / engraved on stainless steel. I want the Brisler Systems to be prominent with laser cut font so that there are no dropouts on the O and A's. My name email and phone number should be engraved black. I would like some cool geometric patterns to cutout on the card to highlight the capabilities of my machine. I will need to files in the end either SVG or dxf of the engrave portion and the cut portion.

```html
<!DOCTYPE html>
<html lang="en">
<head>
<meta charset="utf-8">
<title>Brisler Systems – Steel Business Card</title>
<link href="https://fonts.googleapis.com/css2?family=Allerta+Stencil&family=Arimo:wght@400&display=swap" rel="stylesheet">
<style>
  :root {
    --backdrop: #eee8e2;
    --steel-light: #f1f1f1;
    --steel-mid: #d2d3d4;
    --steel-dark: #a9abad;
    --steel-edge: #8d8f91;
    --engrave: #1b1b1b;
    --cutout-dark: #3a352f;
    --cutout-warm: #b9a58a;
  }
  * { margin: 0; padding: 0; box-sizing: border-box; }
  html, body {
    width: 1200px;
    height: 1200px;
    overflow: hidden;
    background: var(--backdrop);
  }
  .stage {
    position: relative;
    width: 1200px;
    height: 1200px;
    background: var(--backdrop);
  }
  .card {
    position: absolute;
    left: 59px;
    top: 234px;
    width: 1084px;
    height: 733px;
    border-radius: 30px;
    border: 2px solid var(--steel-edge);
    background:
      repeating-linear-gradient(180deg, rgba(255,255,255,0.18) 0 1px, rgba(0,0,0,0.035) 1px 3px),
      linear-gradient(115deg, var(--steel-dark) 0%, var(--steel-mid) 22%, var(--steel-light) 48%, var(--steel-mid) 70%, var(--steel-dark) 100%);
    overflow: hidden;
  }
  .company {
    position: absolute;
    left: 80px;
    top: 215px;
    color: var(--engrave);
    font-family: "Allerta Stencil", sans-serif;
    text-transform: uppercase;
    line-height: 1;
  }
  .company-name {
    display: block;
    font-size: 118px;
    letter-spacing: 1px;
  }
  .company-tagline {
    display: block;
    margin-top: 22px;
    font-size: 62px;
    letter-spacing: 1px;
  }
  .contact {
    position: absolute;
    left: 82px;
    top: 540px;
    list-style: none;
    color: var(--engrave);
    font-family: "Arimo", sans-serif;
    font-size: 33px;
    line-height: 47px;
  }
  .cut-pattern {
    position: absolute;
    left: 672px;
    top: 30px;
    width: 366px;
    height: 662px;
    border-radius: 14px;
    background: linear-gradient(90deg, var(--cutout-dark) 0%, var(--cutout-warm) 45%, var(--cutout-dark) 100%);
    opacity: 0.85;
  }
</style>
</head>
<body>
  <main class="stage">
    <section class="card">
      <h1 class="company">
        <span class="company-name">Brisler</span>
        <span class="company-tagline">Systems</span>
      </h1>
      <ul class="contact">
        <li class="contact-name">Martin Pelko</li>
        <li class="contact-email">martin@mpelkoworks.com</li>
        <li class="contact-phone">417-555-0136</li>
      </ul>
      <div class="cut-pattern" role="img" aria-label="Laser-cut pattern of stacked wavy slot rows through the steel"></div>
    </section>
  </main>
</body>
</html>
```